Website Redesign for Asset Management

We need a full redesign on the website for Velbrook Asset Management. Velbrook is an asset manager that manages both long - only products and alternative investments. We would like to see a clean and innovative website that showcases the products of the firm and the management of the firm.
www.velbrook-example.com
Updates

Output should be in PSD and designer should have groups/layers for the developer to extract the imagesĀ 

Feel free to play with the colours as we are not stuck to current colours.

Target Market(s)

The target market are affluent individuals, pensions, foundations and endowments

Industry/Entity Type

Asset Management

Requirements
Must have
• We like the websites
www.dalvertcourt-example.com
www.quillanfunds-example.com
DO LIKE
http://www.morvatek-example.com/#Home
http://www.dalvertcourt-example.com/who-we-are/principals.html
http://www.ktrellin-example.com/default.aspx
http://www.qp4-example.ca/
http://www.parvenholt-example.com/Home
https://www.lumivaleholdings-example.com/index.asp
http://www.crispell-example.ca/Home_Page.html
http://www.dqrmoxley-example.com/#!contact/c16fm
http://www.fenstraleinvest-example.com/
http://www.oberlyn-example.com/
https://www.quessagroup-example.com/
http://www.mkvor-example.com/
http://www.hadrickgroup-example.com/

Don't Like
http://www.silvertallow-example.com
http://kemble-example.com/
http://rvandolin-example.com/
http://www.ptwilder-example.com/operations_team.html

Also must have a section entitles Alternative Investments

```html
<!DOCTYPE html>
<html lang="en">
<head>
<meta charset="utf-8">
<title>Velbrook Asset Management</title>
<link rel="stylesheet" href="https://fonts.googleapis.com/css2?family=Lato:wght@300;400;700&family=Tinos:wght@400;700&display=swap">
<style>
  :root {
    --brand-blue: #1a4f8a;
    --nav-blue: #1479c4;
    --tab-navy: #0e3a66;
    --ring-navy: #0d3157;
    --text-grey: #666666;
    --footer-grey: #555555;
    --rule: #dcdcdc;
    --white: #ffffff;
    --logo-grey: #9a9a9a;
  }
  * { margin: 0; padding: 0; box-sizing: border-box; }
  html, body { width: 1200px; height: 951px; overflow: hidden; background: var(--white); }
  body { position: relative; font-family: "Lato", Arial, sans-serif; color: var(--text-grey); }

  .hero { position: absolute; left: 0; top: 0; width: 1200px; height: 376px; overflow: hidden; }
  .hero-visual {
    position: absolute; inset: 0;
    background:
      radial-gradient(ellipse at 75% 30%, rgba(70,160,230,.55) 0%, rgba(120,190,240,.25) 40%, rgba(255,255,255,0) 70%),
      radial-gradient(ellipse at 35% 80%, rgba(235,200,185,.55) 0%, rgba(255,255,255,0) 45%),
      linear-gradient(100deg, #f4f6f9 0%, #e9eef4 40%, #d7e7f6 70%, #e8f0f8 100%);
  }
  .brand { position: absolute; left: 206px; top: 38px; display: flex; align-items: center; gap: 8px;
    font-family: "Tinos", serif; font-size: 36px; color: var(--brand-blue); }
  .brand-mark { width: 14px; height: 14px; background: var(--brand-blue); }
  .social { position: absolute; left: 933px; top: 15px; display: flex; gap: 4px; }
  .social span { width: 19px; height: 19px; border: 1.5px solid var(--brand-blue); border-radius: 50%; }
  .tagline { position: absolute; font-family: "Tinos", serif; color: var(--brand-blue);
    font-size: 50px; letter-spacing: 1px; line-height: 1; text-shadow: 0 1px 0 rgba(255,255,255,.7); }
  .tagline-grow { left: 200px; top: 230px; }
  .tagline-preserve { left: 512px; top: 286px; }

  .main-nav { position: absolute; left: 0; top: 376px; width: 1200px; height: 42px; background: var(--nav-blue); }
  .main-nav a { position: absolute; top: 13px; color: var(--white); font-size: 13px; text-decoration: none; white-space: nowrap; }
  .main-nav a.current { font-weight: 700; }
  .main-nav svg { margin-left: 4px; vertical-align: 1px; }

  .sub-tabs { position: absolute; left: 200px; top: 443px; width: 802px; height: 26px; display: flex; }
  .sub-tabs a { flex: 1; background: var(--tab-navy); color: var(--white); font-family: "Tinos", serif;
    font-size: 15px; text-align: center; line-height: 26px; text-decoration: none; border-right: 1px solid var(--white); white-space: nowrap; }
  .sub-tabs a:last-child { border-right: none; }

  .intro { position: absolute; left: 200px; top: 483px; width: 800px; font-size: 12.3px; font-weight: 300; line-height: 15.3px; color: var(--text-grey); }
  .intro p { margin-bottom: 5px; }
  .intro p:first-child { padding-left: 3px; }

  .rule { position: absolute; left: 0; width: 1200px; height: 1px; background: var(--rule); }

  .section-title { position: absolute; left: 201px; top: 629px; font-family: "Tinos", serif; font-size: 24px; font-weight: 400; color: var(--brand-blue); }
  .option { position: absolute; top: 674px; width: 120px; text-align: center; }
  .option-ring { width: 108px; height: 108px; margin: 0 auto; border-radius: 50%; background: var(--ring-navy); padding: 7px;
    box-shadow: 0 3px 5px rgba(0,0,0,.15); }
  .option-photo { width: 94px; height: 94px; border-radius: 50%; }
  .option-shadow { width: 60px; height: 4px; margin: 8px auto 0; border-radius: 50%; background: rgba(0,0,0,.08); }
  .option-label { margin-top: 8px; font-family: "Tinos", serif; font-size: 17px; color: #222; }

  .footer-links { position: absolute; left: 201px; top: 871px; font-size: 12px; color: var(--footer-grey); }
  .footer-links a { color: var(--footer-grey); text-decoration: none; }
  .footer-company { position: absolute; left: 513px; top: 871px; font-size: 12px; color: var(--footer-grey); }
  .disclaimer { position: absolute; left: 548px; top: 917px; font-family: "Tinos", serif; font-size: 15.5px; color: #111; text-decoration: underline; }
  .footer-brand { position: absolute; left: 866px; top: 886px; display: flex; align-items: center; gap: 6px;
    font-family: "Tinos", serif; font-size: 28px; color: var(--logo-grey); }
  .footer-brand .brand-mark { background: var(--logo-grey); width: 11px; height: 11px; }
  .copyright { position: absolute; left: 871px; top: 922px; font-size: 12px; color: var(--footer-grey); }
</style>
</head>
<body>
  <header class="hero">
    <div class="hero-visual" role="img" aria-label="Photo of a hand touching a tablet showing a blue bar chart"></div>
    <div class="brand"><span class="brand-mark"></span>Velbrook</div>
    <div class="social" aria-label="Social links"><span></span><span></span><span></span></div>
    <h1 class="tagline tagline-grow">GROWING WEALTH</h1>
    <p class="tagline tagline-preserve">PRESERVING CAPITAL</p>
  </header>

  <nav class="main-nav">
    <a class="current" style="left:266px">Home<svg width="7" height="4"><path d="M0 0h7L3.5 4z" fill="#fff"/></svg></a>
    <a style="left:342px">Profile<svg width="4" height="7"><path d="M0 0v7l4-3.5z" fill="#fff"/></svg></a>
    <a style="left:422px">Investment Process<svg width="4" height="7"><path d="M0 0v7l4-3.5z" fill="#fff"/></svg></a>
    <a style="left:574px">Investment Solutions<svg width="4" height="7"><path d="M0 0v7l4-3.5z" fill="#fff"/></svg></a>
    <a style="left:735px">News &amp; Views<svg width="4" height="7"><path d="M0 0v7l4-3.5z" fill="#fff"/></svg></a>
    <a style="left:857px">Contact<svg width="4" height="7"><path d="M0 0v7l4-3.5z" fill="#fff"/></svg></a>
  </nav>

  <nav class="sub-tabs">
    <a>Introduction</a><a>Corprate Identity</a><a>Trademark Diffrance</a><a>Industry Associations</a><a>Governance</a><a>Service Partners</a>
  </nav>

  <section class="intro">
    <p>Velbrook Asset Management Inc. is an independent and focused portfolio management firm servicing high net worth families, foundations and institutions. Balancing growth with capital preservation, Velbrook has established itself as a premier North American investment manager.</p>
    <p>As an independent firm established in January 1998, Velbrook has no affiliation or gainful association to prejudice the investment decision-making process. Our performance track record dates back to 1993 for our Canadian Equity mandate and our proven Core-Balance™ investment philosophy has been virtually unchanged since that time. The philosophical foundation is to strictly and tangibly align Velbrook’s interests with those of clients and incentive fees replace more traditional high management fees.</p>
  </section>

  <div class="rule" style="top:615px"></div>

  <h2 class="section-title">Alternative Investments</h2>
  <div class="option" style="left:258px"><div class="option-ring"><div class="option-photo" role="img" aria-label="Pen resting on financial charts" style="background:radial-gradient(circle at 40% 40%,#dfe6ef,#8fa6c4)"></div></div><div class="option-shadow"></div><div class="option-label">1. Option</div></div>
  <div class="option" style="left:392px"><div class="option-ring"><div class="option-photo" role="img" aria-label="Stacks of gold coins" style="background:radial-gradient(circle at 40% 50%,#e6c463,#b88a2a 60%,#e8ecf2)"></div></div><div class="option-shadow"></div><div class="option-label">2. Option</div></div>
  <div class="option" style="left:526px"><div class="option-ring"><div class="option-photo" role="img" aria-label="Stock market chart on a dark screen" style="background:radial-gradient(circle at 50% 50%,#3a3f9a,#141a4a)"></div></div><div class="option-shadow"></div><div class="option-label">3. Option</div></div>
  <div class="option" style="left:659px"><div class="option-ring"><div class="option-photo" role="img" aria-label="Handshake with banknotes" style="background:radial-gradient(circle at 50% 45%,#c9cbb8,#7a5a45 60%,#2a2a2a)"></div></div><div class="option-shadow"></div><div class="option-label">4. Option</div></div>
  <div class="option" style="left:793px"><div class="option-ring"><div class="option-photo" role="img" aria-label="Hand placing a coin among growing plants" style="background:linear-gradient(180deg,#9fc4e8 0%,#d9e7f2 50%,#7aa04a 75%,#c9a56a 100%)"></div></div><div class="option-shadow"></div><div class="option-label">5. Option</div></div>

  <div class="rule" style="top:853px"></div>

  <footer>
    <div class="footer-links"><a>Privacy Policy</a> &nbsp;| <a>Careers</a> &nbsp;| <a>Contact Us</a></div>
    <div class="footer-company">Velbrook Asset Management Inc.</div>
    <a class="disclaimer">DISCLAIMER&nbsp;</a>
    <div class="footer-brand"><span class="brand-mark"></span>Velbrook</div>
    <div class="copyright">All rights reserved ©2014</div>
  </footer>
</body>
</html>
```